KVT Business Cards

We require business cards for our business. We would like a matte black back to the card, with our logo centred in the middle. The front side of the card is open to design.

Target Market(s)

Clients looking for legal services (professional)

Industry/Entity Type

Legal

Contact Information for Business Card

Boris Telemark
Partner
Mobile: 0438 715 642
Email: boris@kvtlaw.co
Website: www.kvtlaw.co
Level 3, 118 Wexbury Street
Sydney NSW 2000

Font styles to use
Other font styles liked:
• Avenir

Colors
f04a50
ffffff
1b1b1b

Requirements
Must have
• Black back with logo included in the centre of the card.
• Our font is Avenir.

```html
<!DOCTYPE html>
<html lang="en">
<head>
<meta charset="utf-8">
<title>KVT Legal – Business Cards</title>
<link rel="stylesheet" href="https://fonts.googleapis.com/css2?family=Nunito+Sans:wght@400;600;700&display=swap">
<style>
  :root {
    --stage: #3a3d40;
    --card-black: #1b1b1b;
    --card-deep: #111111;
    --panel: #242424;
    --red: #f04a50;
    --red-deep: #c4141c;
    --white: #ffffff;
    --muted: #e8e8e8;
  }
  * { margin: 0; padding: 0; box-sizing: border-box; }
  html, body {
    width: 1200px; height: 994px; overflow: hidden;
    background: var(--stage);
    font-family: "Nunito Sans", "Avenir", sans-serif;
  }
  .stage { position: relative; width: 1200px; height: 994px; }

  .card {
    position: absolute;
    width: 680px; height: 389px;
    background: radial-gradient(ellipse at 50% 45%, #232323 0%, var(--card-black) 55%, var(--card-deep) 100%);
    box-shadow: 0 24px 50px rgba(0,0,0,.45);
    overflow: hidden;
  }
  .card--back { left: 70px; top: 70px; }
  .card--front { left: 450px; top: 530px; }

  .brand {
    position: absolute;
    display: flex; align-items: center; gap: 12px;
    color: var(--white);
    font-weight: 700;
    letter-spacing: 1px;
    text-transform: uppercase;
  }
  .brand__mark { background: var(--red); }
  .card--back .brand { left: 50%; top: 50%; transform: translate(-50%, -50%); font-size: 30px; }
  .card--back .brand__mark { width: 26px; height: 26px; }
  .card--front .brand { right: 58px; top: 62px; font-size: 26px; }
  .card--front .brand__mark { width: 22px; height: 22px; }

  .card__decor {
    position: absolute;
    background: linear-gradient(135deg, var(--panel) 0%, #2a1a1b 60%, rgba(240,74,80,.35) 100%);
  }
  .card__decor--top { left: 0; top: 0; width: 340px; height: 180px; }
  .card__decor--bottom {
    right: 0; bottom: 0; width: 340px; height: 180px;
    background: linear-gradient(315deg, var(--panel) 0%, #2a1a1b 60%, rgba(240,74,80,.35) 100%);
  }

  .contact {
    position: absolute; left: 44px; top: 236px;
    color: var(--white);
    font-size: 13px; line-height: 1;
  }
  .contact__name {
    display: flex; align-items: center; gap: 8px;
    font-weight: 600; text-transform: uppercase; letter-spacing: .5px;
    margin-bottom: 9px;
  }
  .contact__role {
    background: var(--white); color: var(--red);
    font-size: 10px; font-weight: 700;
    padding: 3px 7px; border-radius: 10px;
  }
  .contact__row { display: flex; align-items: flex-start; gap: 10px; margin-bottom: 8px; color: var(--muted); }
  .contact__row svg { width: 14px; height: 14px; flex: none; stroke: var(--white); fill: none; stroke-width: 1.4; }
  .contact__label { margin-right: 4px; }
  .contact__address { line-height: 1.25; }
</style>
</head>
<body>
<main class="stage">

  <section class="card card--back" aria-label="Card back">
    <div class="brand"><span class="brand__mark"></span>KVT Legal</div>
  </section>

  <section class="card card--front" aria-label="Card front">
    <div class="card__decor card__decor--top" role="img" aria-label="Decorative dark panel with red accents"></div>
    <div class="card__decor card__decor--bottom" role="img" aria-label="Decorative dark panel with red accents"></div>

    <div class="brand"><span class="brand__mark"></span>KVT Legal</div>

    <div class="contact">
      <div class="contact__row contact__name">
        <svg viewBox="0 0 16 16"><circle cx="8" cy="5" r="3"/><path d="M2 15c0-3.5 3-5 6-5s6 1.5 6 5z"/></svg>
        Boris Telemark <span class="contact__role">PARTNER</span>
      </div>
      <div class="contact__row">
        <svg viewBox="0 0 16 16"><circle cx="8" cy="8" r="7"/><path d="M5.5 4.5l1.5 2-1 1c.5 1 1.5 2 2.5 2.5l1-1 2 1.5-1 1.5c-2.5 0-5.5-3-5.5-5.5z"/></svg>
        <span><span class="contact__label">Mobile:</span> 0438 715 642</span>
      </div>
      <div class="contact__row">
        <svg viewBox="0 0 16 16"><rect x="1" y="3.5" width="14" height="9"/><path d="M1 3.5l7 5 7-5"/></svg>
        <span><span class="contact__label">Email:</span> boris@kvtlaw.co</span>
      </div>
      <div class="contact__row">
        <svg viewBox="0 0 16 16"><circle cx="8" cy="8" r="7"/><ellipse cx="8" cy="8" rx="3" ry="7"/><path d="M1 8h14M2.5 4.5h11M2.5 11.5h11"/></svg>
        <span><span class="contact__label">Website:</span> www.kvtlaw.co</span>
      </div>
      <div class="contact__row">
        <svg viewBox="0 0 16 16"><path d="M8 15s-5-5-5-8.5a5 5 0 0110 0C13 10 8 15 8 15z"/><circle cx="8" cy="6.5" r="1.8"/></svg>
        <span class="contact__address">LEVEL 3, 118 Wexbury Street<br>Sydney , NSW 2000</span>
      </div>
    </div>
  </section>

</main>
</body>
</html>
```